Flooring & Interior Design showroom

Just bought this business- Kestrel Lane Flooring & Interiors. Love our logo (we are on Kestrel Lane )and colors
Forest green, gold and black
Love that the back lists everything we do. We no longer have plenotilex but need to add in LVP/ SPC and need to take out vantor shadehub logo at the bottom and use the quib logo instead (maybe? open to suggestions)

Not in love with our cards- I want a higher end look
I hate the gradient poop color we have now.
Would love if they were all black - maybe or ??
or had a foil or embossing?

```html
<!DOCTYPE html>
<html lang="en">
<head>
<meta charset="utf-8">
<title>Kestrel Lane Flooring &amp; Interiors — Business Card</title>
<link rel="stylesheet" href="https://fonts.googleapis.com/css2?family=Arimo:wght@400;700&family=Cinzel:wght@600;700&display=swap">
<style>
  :root {
    --stage: #2b2b2b;
    --forest: #1f5534;
    --forest-deep: #184a2c;
    --tan: #d9a07c;
    --gold: #ead79d;
    --ink: #060606;
    --paper: #f7f7f7;
    --grey: #c9c9c9;
    --white: #ffffff;
  }
  * { box-sizing: border-box; margin: 0; padding: 0; }
  html, body { width: 1200px; height: 1015px; overflow: hidden; }
  body {
    background: var(--stage);
    font-family: "Arimo", Arial, sans-serif;
    position: relative;
  }
  .card {
    position: absolute;
    left: 250px;
    width: 700px;
    height: 400px;
    overflow: hidden;
    box-shadow: 0 10px 30px rgba(0,0,0,.45);
  }
  .card--front { top: 55px; background: var(--paper); }
  .card--back { top: 560px; background: var(--ink); }
  .card__bands { position: absolute; inset: 0; width: 700px; height: 400px; }

  .brand {
    position: absolute;
    display: flex;
    align-items: center;
    gap: 14px;
    font-family: "Arimo", Arial, sans-serif;
    font-weight: 700;
    font-size: 24px;
    line-height: 30px;
    width: 330px;
  }
  .brand__dot {
    width: 34px; height: 34px;
    border-radius: 50%;
    flex: none;
    background: currentColor;
  }
  .card--front .brand { left: 50px; top: 70px; color: var(--forest); }
  .card--back .brand { left: 48px; top: 122px; color: var(--gold); }

  .partner {
    position: absolute;
    top: 70px;
    font-family: "Arimo", Arial, sans-serif;
    font-weight: 700;
  }
  .partner--fenwright { left: 405px; font-size: 22px; color: var(--forest); }
  .partner--quib { left: 560px; font-size: 28px; color: var(--ink); top: 64px; }

  .tagline {
    position: absolute;
    font-size: 15px;
    letter-spacing: .5px;
    color: var(--forest-deep);
  }
  .card--front .tagline { left: 448px; top: 154px; }
  .card--back .tagline { left: 70px; top: 262px; }

  .services {
    position: absolute;
    list-style: none;
    color: var(--white);
    font-size: 19px;
    line-height: 25px;
  }
  .services li::before {
    content: "";
    display: inline-block;
    width: 7px; height: 7px;
    border-radius: 50%;
    background: var(--tan);
    margin-right: 9px;
    vertical-align: middle;
  }
  .services--a { left: 70px; top: 228px; }
  .services--b { left: 290px; top: 212px; }
  .services--c { left: 515px; top: 190px; }

  .person { position: absolute; right: 40px; top: 72px; text-align: right; }
  .person__name {
    font-family: "Cinzel", Georgia, serif;
    font-weight: 700;
    font-size: 30px;
    letter-spacing: 2px;
    color: var(--gold);
  }
  .person__role { font-size: 17px; color: var(--grey); margin-top: 2px; }

  .contact {
    position: absolute;
    left: 70px; top: 294px;
    list-style: none;
    color: var(--white);
    font-size: 17px;
    line-height: 19px;
  }
  .contact li { display: flex; align-items: center; gap: 8px; }
  .contact svg { width: 15px; height: 15px; flex: none; }

  .address {
    position: absolute;
    right: 40px; top: 262px;
    color: var(--white);
    font-size: 17px;
    line-height: 22px;
    text-align: right;
  }
  .address__licence { margin-top: 18px; }
</style>
</head>
<body>

<section class="card card--front" aria-label="Card front">
  <svg class="card__bands" viewBox="0 0 700 400" aria-hidden="true">
    <path d="M0 188 H340 C362 188 362 148 390 148 H700 V400 H0 Z" fill="var(--tan)"/>
    <path d="M0 198 H360 C382 198 386 178 408 178 H700 V400 H0 Z" fill="var(--forest)"/>
  </svg>

  <div class="brand">
    <span class="brand__dot" aria-hidden="true"></span>
    <span class="brand__name">Kestrel Lane Flooring &amp; Interiors</span>
  </div>

  <span class="partner partner--fenwright">Fenwright</span>
  <span class="partner partner--quib">quib</span>

  <p class="tagline">Home Town Service Since 1979</p>

  <ul class="services services--a">
    <li>Area Rugs</li><li>Bed Spreads</li><li>Blinds</li><li>Carpet</li><li>Cork</li><li>Fabric</li>
  </ul>
  <ul class="services services--b">
    <li>Hardwood</li><li>Laminate</li><li>LVP/ SPC</li><li>Motorized Shades</li><li>Pillows</li><li>Sand &amp; refinish</li>
  </ul>
  <ul class="services services--c">
    <li>Sheers</li><li>Shutters</li><li>Upholstery</li><li>Valances</li><li>Verticals</li><li>Vinyl</li>
  </ul>
</section>

<section class="card card--back" aria-label="Card back">
  <svg class="card__bands" viewBox="0 0 700 400" aria-hidden="true">
    <path d="M0 252 H385 C406 252 410 226 432 226 H700 V400 H0 Z" fill="var(--tan)"/>
    <path d="M0 284 H400 C420 284 430 234 452 234 H700 V400 H0 Z" fill="var(--forest)"/>
  </svg>

  <div class="brand">
    <span class="brand__dot" aria-hidden="true"></span>
    <span class="brand__name">Kestrel Lane Flooring &amp; Interiors</span>
  </div>

  <div class="person">
    <p class="person__name">OWEN CASTELL</p>
    <p class="person__role">Salesperson</p>
  </div>

  <p class="tagline">Home Town Service Since 1979</p>

  <ul class="contact">
    <li>
      <svg viewBox="0 0 16 16" aria-hidden="true"><path d="M3 1.5 L6 1.5 L7 5 L5.2 6.3 C6 8.2 7.8 10 9.7 10.8 L11 9 L14.5 10 L14.5 13 C14.5 14 13.8 14.5 13 14.5 C6.7 14.2 1.8 9.3 1.5 3 C1.5 2.2 2 1.5 3 1.5 Z" fill="var(--white)"/></svg>
      555.310.0142
    </li>
    <li>
      <svg viewBox="0 0 16 16" aria-hidden="true"><rect x="4" y="1" width="8" height="14" rx="1.5" fill="none" stroke="var(--white)" stroke-width="1.6"/><circle cx="8" cy="12.3" r="0.9" fill="var(--white)"/></svg>
      555.204.7731
    </li>
    <li>
      <svg viewBox="0 0 16 16" aria-hidden="true"><rect x="4" y="1" width="8" height="5" fill="var(--white)"/><rect x="1" y="6" width="14" height="6" rx="1" fill="var(--white)"/><rect x="4" y="10" width="8" height="5" fill="var(--forest)" stroke="var(--white)" stroke-width="1.2"/></svg>
      555.310.0188
    </li>
    <li>
      <svg viewBox="0 0 16 16" aria-hidden="true"><rect x="1" y="3" width="14" height="10" fill="var(--white)"/><path d="M1 3 L8 9 L15 3" fill="none" stroke="var(--forest)" stroke-width="1.3"/></svg>
      owen@kestrellaneflooring.com
    </li>
    <li>
      <svg viewBox="0 0 16 16" aria-hidden="true"><g fill="none" stroke="var(--white)" stroke-width="1.2"><circle cx="8" cy="8" r="6.5"/><ellipse cx="8" cy="8" rx="3" ry="6.5"/><path d="M1.5 8 H14.5 M2.5 4.8 H13.5 M2.5 11.2 H13.5"/></g></svg>
      www.kestrellaneflooring.com
    </li>
  </ul>

  <div class="address">
    <p>218 Kestrel Lane</p>
    <p>Harbor Glen CA 90412</p>
    <p class="address__licence">CA Lic: 481736</p>
  </div>
</section>

</body>
</html>
```